Wedding Vows Poster for a Frame (anniversary gift )

I need an 8 X11 copy of both or wedding vows that I can frame in a classy and timeless modern font to frame for our house .

see file attach for text (vows)

project is now close thank you for all your help

```html
<!DOCTYPE html>
<html lang="en">
<head>
<meta charset="utf-8">
<title>Daniel to Claire – Wedding Vows</title>
<link rel="stylesheet" href="https://fonts.googleapis.com/css2?family=Great+Vibes&family=Tinos:wght@400&display=swap">
<style>
  :root {
    --paper: #ffffff;
    --magenta: #b8174f;
    --magenta-deep: #8e0f3c;
    --magenta-light: #d9356a;
    --lime: #b5cf2d;
    --lime-light: #d3e24a;
    --gold: #e9b52c;
    --gold-light: #f8dc74;
    --gold-deep: #b7821a;
    --ink: #1a1a1a;
    --violet: #7a1f88;
    --photo-green: #6e9a3a;
    --photo-dark: #2c3a1c;
  }
  * { margin: 0; padding: 0; box-sizing: border-box; }
  html, body { width: 872px; height: 1200px; overflow: hidden; background: var(--paper); }
  .poster { position: relative; width: 872px; height: 1200px; background: var(--paper); overflow: hidden; }

  .header-pattern {
    position: absolute; left: 0; top: 0; width: 872px; height: 260px;
    background: linear-gradient(135deg, var(--magenta-deep) 0%, var(--magenta) 45%, var(--magenta-light) 75%, var(--magenta) 100%);
  }
  .title-band {
    position: absolute; left: 0; top: 69px; width: 872px; height: 94px;
    background: var(--lime);
  }
  .title {
    position: absolute; left: 48px; top: 82px;
    font-family: "Great Vibes", cursive;
    font-size: 58px; line-height: 1; color: var(--ink);
    text-shadow: -2px -2px 0 #fff, 2px -2px 0 #fff, -2px 2px 0 #fff, 2px 2px 0 #fff, 3px 4px 4px rgba(0,0,0,.45);
  }
  .title .joiner { color: var(--violet); }
  .couple-photo {
    position: absolute; left: 594px; top: 48px; width: 225px; height: 150px;
    background: radial-gradient(ellipse at 55% 55%, var(--photo-green) 0%, var(--photo-dark) 100%);
    border: 2px solid #fff;
  }
  .ribbon-line {
    position: absolute; left: 0; top: 256px; width: 872px; height: 10px;
    background: linear-gradient(180deg, var(--gold-light), var(--gold) 50%, var(--gold-deep));
  }
  .ribbon-bow {
    position: absolute; left: 386px; top: 238px; width: 100px; height: 92px;
    background: radial-gradient(ellipse at 50% 30%, var(--gold-light), var(--gold) 55%, var(--gold-deep));
    border-radius: 40% 40% 30% 30%;
  }

  .vows {
    position: absolute; left: 40px; top: 358px; width: 792px;
    font-family: "Tinos", "Times New Roman", serif;
    font-size: 16.5px; line-height: 23.6px; color: var(--ink); text-align: center;
  }
  .vows p { margin: 0; }
  .vows .gap { margin-top: 23.6px; }

  .footer-stripe {
    position: absolute; left: 0; top: 1104px; width: 872px; height: 24px;
    background: linear-gradient(90deg, var(--magenta), var(--magenta-light), var(--magenta));
  }
  .footer-pattern {
    position: absolute; left: 0; top: 1130px; width: 872px; height: 70px;
    background: linear-gradient(90deg, var(--lime), var(--lime-light), var(--lime));
  }
</style>
</head>
<body>
<main class="poster">
  <div class="header-pattern" role="img" aria-label="Magenta pattern of hearts and flowers"></div>
  <div class="title-band"></div>
  <h1 class="title">Daniel <span class="joiner">to</span> Claire</h1>
  <div class="couple-photo" role="img" aria-label="Photo of a bride and groom holding hands"></div>
  <div class="ribbon-line"></div>
  <div class="ribbon-bow" role="img" aria-label="Gold ribbon bow"></div>

  <section class="vows">
    <p>Three years ago I fell in love with you on our journey trough Peru, your love for life , your drive,<br>
    your beautiful smile, and natural beauty were at the time what got my attention.<br>
    Now that I know much more about you I have realize how much<br>
    more complete of an individual you are.<br>
    For a long time I wish I had meet you before however only now I can appreciate you fully.<br>
    I love you Claire<br>
    "This ring represents my commitment to you as your partner and to our marriage.<br>
    As your partner I am committed to a life where we can have it<br>
    all.&nbsp; By all I mean an amazing relationship where we can share a fulfilling life together.<br>
    As your husband I promise to be loyal and give you the best that I<br>
    can, protect and cherish you I will always be there for you trough good and hard time.</p>
    <p class="gap">I will grow old with you and love you forever.</p>
    <p class="gap">Daniel</p>
    <p class="gap">Claire to Daniel</p>
    <p class="gap">"This ring represents my commitment to you as your partner and to our marriage.<br>
    As your partner I promise to always do my best to support, respect,<br>
    be compassionate and loving to you.&nbsp; And as your wife,<br>
    I promise to always to my best to be honest, trust worthy trust<br>
    and during challenging times to have the faith that<br>
    we will somehow overcome it and be even stronger on the other side.</p>
    <p class="gap">Dani, you are my favorite person, I love you with all my heart and<br>
    I am so very proud to be your wife. "</p>
    <p class="gap">Love always,<br>c</p>
  </section>

  <div class="footer-stripe" role="img" aria-label="Magenta patterned stripe"></div>
  <div class="footer-pattern" role="img" aria-label="Lime pattern of hearts and flowers"></div>
</main>
</body>
</html>
```